New web design needed for our company

We need our website designing, it needs to be professional and look creative,
We are a plumbing and heating company called Brackwell Flow's (www.brackwellflows.co.uk)
I like this site design also some of the following maybe:
https://www.tindermoorwarmth.com/
http://www.quorvapower.co.uk

Please let me know when you want our logo files as it wont let me upload them

The design will require coding once the design is complete, i havent paid for this yet as i want to be sure the design is good before i commit.

The template needs to look professional and look like one of the leading companies.
The site will consist of all the features this site has https://www.tindermoorwarmth.com/

I like a modern design with the latest technology.

Must have a customer login page and a my account area

Target Market(s)

Everyone

Industry/Entity Type

Plumbing

Coding

Coded - Design and coding required

Number of Pages Required

5+ page

Font styles to use
Other font styles liked:
• whatever suites

Requirements
Must have
• The design will require coding once the design is complete, i havent paid for this yet as i want to be sure the design is good before i commit.
• The template needs to look professional and look like one of the leading companies.
• The site will consist of all the features this site has https://www.tindermoorwarmth.com/
• I like a modern design with the latest technology.
• Must have a customer login page and a my account area
Nice to have
• inspirational and different
Should not have
• plain boring designs like most plumbing websites, needs to be inspiring and attract people from first sight.

```html
<!DOCTYPE html>
<html lang="en">
<head>
<meta charset="utf-8">
<title>Brackwell Flow's – Your Local Experts</title>
<link rel="stylesheet" href="https://fonts.googleapis.com/css2?family=Lato:wght@400;700;900&family=Open+Sans:wght@400;600;700&display=swap">
<style>
:root{
  --navy:#1c2f6e;
  --orange:#f4583a;
  --ink:#333;
  --muted:#555;
  --soft:#8a8a8a;
  --topbar:#e9e9e9;
  --band:#efefef;
  --footer:#f1f1f1;
  --white:#fff;
}
*{box-sizing:border-box;margin:0;padding:0}
html,body{width:1200px;height:2311px;overflow:hidden}
body{position:relative;background:var(--white);font-family:"Open Sans",Arial,sans-serif;color:var(--ink)}
.abs{position:absolute}

/* top bar */
.topbar{left:0;top:0;width:1200px;height:36px;background:var(--topbar)}
.account-link{left:80px;top:10px;font-size:12px;color:#222;display:flex;align-items:center;gap:6px;white-space:nowrap}
.search{left:895px;top:8px;width:222px;height:22px;background:var(--white);border:1px solid #d5d5d5}
.search svg{position:absolute;right:6px;top:4px}

/* header */
.header{left:0;top:36px;width:1200px;height:103px;background:var(--white)}
.brand{left:80px;top:62px;display:flex;align-items:center;gap:10px;white-space:nowrap}
.brand-mark{width:22px;height:22px;border-radius:50%;background:var(--orange)}
.brand-name{font-family:"Lato",Arial,sans-serif;font-weight:900;font-size:32px;color:var(--navy);letter-spacing:-.5px}
.brand-tag{left:118px;top:100px;font-size:12px;color:var(--navy);white-space:nowrap}
.nav{left:442px;top:72px;display:flex;align-items:center;font-size:13.5px;color:#333;white-space:nowrap}
.nav a{color:inherit;text-decoration:none;display:block;height:36px;line-height:36px;margin-right:20px}
.nav a:last-child{margin-right:0}
.nav a.active{background:var(--orange);color:var(--white);padding:0 12px;margin-right:14px}
.cart{left:1063px;top:78px;display:flex;align-items:center}
.cart-badge{width:28px;height:28px;border-radius:50%;background:var(--orange);color:#fff;font-size:13px;font-weight:700;text-align:center;line-height:28px;margin-left:-4px}

/* hero */
.hero{left:0;top:139px;width:1200px;height:315px;background:linear-gradient(100deg,#6d7378 0%,#3f464d 45%,#2d3238 100%)}
.hero-tag{left:644px;height:52px;line-height:52px;padding:0 17px;color:#fff;font-family:"Lato",Arial,sans-serif;font-weight:700;font-size:25px;letter-spacing:.5px;white-space:nowrap}
.hero-tag.primary{top:242px;width:476px;background:var(--navy)}
.hero-tag.secondary{top:302px;background:var(--orange)}

/* service categories */
.services{left:0;top:454px;width:1200px;height:241px;background:var(--band)}
.service{position:absolute;top:36px;width:180px;text-align:center}
.service-tile{width:123px;height:120px;margin:0 auto;background:#fff;border:1px solid #ddd;border-radius:16px;display:flex;align-items:center;justify-content:center}
.service-name{margin-top:18px;font-family:"Lato",Arial,sans-serif;font-weight:700;font-size:16px;color:#111;letter-spacing:.2px;white-space:nowrap}

/* promos */
.promo{top:769px;width:485px;height:309px;overflow:hidden}
.promo-boiler{left:80px;background:linear-gradient(180deg,#d9dfe6 0%,#9aa9c4 45%,#2a4796 80%,#1c3a8c 100%)}
.promo-boiler-title{left:36px;top:185px;color:#fff;font-family:"Lato",Arial,sans-serif;font-weight:700;font-size:40px;line-height:48px;white-space:nowrap}
.promo-move{left:630px;background:linear-gradient(110deg,#9a9a94 0%,#c8c3b6 55%,#d8cdb8 100%)}
.promo-move-title{left:29px;top:44px;color:#fff;font-family:"Lato",Arial,sans-serif;font-weight:900;font-size:35px;white-space:nowrap}
.promo-move-text{left:29px;top:94px;color:#fff;font-size:20px;line-height:28px;width:340px}
.btn-arrow{left:29px;top:175px}

/* testimonial */
.testimonial{left:0;top:1164px;width:1200px;height:418px;background:linear-gradient(90deg,#e7e9ec 0%,#d8dce2 40%,#a9b4c3 70%,#c9ced6 100%)}
.quote-card{left:85px;top:1234px;width:536px;height:228px;background:#fff;padding:34px 36px 34px 48px}
.quote-title{font-family:"Lato",Arial,sans-serif;font-size:23px;font-weight:400;letter-spacing:.5px;color:#222}
.quote-text{margin-top:18px;font-size:13.5px;line-height:26px;color:#555;padding-left:2px}
.quote-mark{left:105px;top:1314px;color:var(--orange);font-size:24px;font-family:Georgia,serif;font-weight:700}
.quote-pointer{left:140px;top:1461px}
.avatar{left:132px;top:1488px;width:51px;height:51px;border-radius:50%;background:#7b6f68;border:2px solid #fff}
.client-name{left:194px;top:1497px;font-size:14px;font-weight:700;color:var(--navy);white-space:nowrap}
.client-place{left:194px;top:1517px;font-size:11px;color:var(--soft);white-space:nowrap}

/* featured */
.footer-bg{left:0;top:1911px;width:1200px;height:356px;background:var(--footer)}
.featured{left:80px;top:1640px;width:1040px;height:336px;background:#fff}
.featured-title{left:97px;top:1656px;font-family:"Lato",Arial,sans-serif;font-size:23px;font-weight:400;letter-spacing:.5px;color:#222;white-space:nowrap}
.work{position:absolute;top:1714px;width:230px}
.work-photo{width:230px;height:108px}
.work-title{margin-top:21px;font-family:"Lato",Arial,sans-serif;font-weight:700;font-size:16px;color:var(--orange);letter-spacing:.3px;white-space:nowrap}
.work-text{margin-top:10px;font-size:12.5px;line-height:19.5px;color:#444}

/* footer */
.footer-col{position:absolute;top:2021px}
.footer-heading{font-family:"Lato",Arial,sans-serif;font-weight:700;font-size:16px;color:var(--navy);letter-spacing:.4px;white-space:nowrap}
.footer-links{list-style:none;margin-top:18px}
.footer-links li{font-size:13.5px;color:#444;height:28.2px;white-space:nowrap}
.legal{left:0;top:2267px;width:1200px;height:44px;background:#fff;border-top:1px solid #ddd}
.legal-left{left:93px;top:2279px;font-size:12.5px;color:#444;display:flex;gap:22px;white-space:nowrap}
.legal-right{left:598px;top:2280px;font-size:12.5px;color:#444;white-space:nowrap}
</style>
</head>
<body>

<div class="abs topbar"></div>
<div class="abs account-link">
  <svg width="12" height="12" viewBox="0 0 12 12"><circle cx="6" cy="3.5" r="3" fill="#222"/><path d="M0 12c0-4 3-5.5 6-5.5s6 1.5 6 5.5z" fill="#222"/></svg>
  My Account:&nbsp; Sign In or Register
</div>
<div class="abs search">
  <svg width="13" height="13" viewBox="0 0 13 13"><circle cx="5.5" cy="5.5" r="4" fill="none" stroke="#222" stroke-width="2"/><path d="M8.5 8.5l3.5 3.5" stroke="#222" stroke-width="2.2"/></svg>
</div>

<header class="abs header"></header>
<div class="abs brand"><span class="brand-mark"></span><span class="brand-name">Brackwell Flow's</span></div>
<div class="abs brand-tag">Your Local Experts</div>
<nav class="abs nav">
  <a class="active" href="#">At Home</a>
  <a href="#">Services</a>
  <a href="#">Emergencies</a>
  <a href="#">Business Customers</a>
  <a href="#">Flow Care</a>
  <a href="#">Help &amp; Support</a>
</nav>
<div class="abs cart">
  <svg width="30" height="24" viewBox="0 0 30 24"><path d="M1 2h5l4 13h14l3-9H8" fill="none" stroke="#222" stroke-width="2.5"/><path d="M8 6h19l-3 9H10z" fill="#222"/><circle cx="12" cy="20" r="2.3" fill="#222"/><circle cx="22" cy="20" r="2.3" fill="#222"/></svg>
  <span class="cart-badge">0</span>
</div>

<section class="abs hero" role="img" aria-label="Photo of a plumber tightening a chrome pipe with a red wrench"></section>
<div class="abs hero-tag primary">BOILER REPAIRS &amp; MAINTENANCE</div>
<div class="abs hero-tag secondary">MORE ABOUT COMPANY</div>

<section class="abs services">
  <div class="service" style="left:51px">
    <div class="service-tile"><svg width="44" height="44" viewBox="0 0 44 44"><path d="M8 6h10v16a4 4 0 0 0 8 0V6h10v16a14 14 0 0 1-28 0z" fill="var(--navy)"/><rect x="4" y="6" width="18" height="6" fill="var(--navy)"/><rect x="22" y="6" width="18" height="6" fill="var(--navy)"/></svg></div>
    <div class="service-name">PLUMBFLOW'S (48)</div>
  </div>
  <div class="service" style="left:231px">
    <div class="service-tile"><svg width="40" height="44" viewBox="0 0 40 44"><rect x="6" y="4" width="20" height="36" rx="3" fill="var(--navy)"/><rect x="10" y="9" width="12" height="10" fill="#fff"/><path d="M26 16h4a3 3 0 0 1 3 3v14a2 2 0 0 0 4 0V12l-5-5" fill="none" stroke="var(--navy)" stroke-width="3"/></svg></div>
    <div class="service-name">GASFLOW'S (13)</div>
  </div>
  <div class="service" style="left:411px">
    <div class="service-tile"><svg width="48" height="44" viewBox="0 0 48 44"><rect x="4" y="8" width="20" height="16" rx="3" fill="var(--navy)"/><path d="M24 14l10 6-4 4z" fill="var(--navy)"/><circle cx="36" cy="30" r="6" fill="var(--navy)"/><circle cx="28" cy="36" r="4" fill="var(--navy)"/></svg></div>
    <div class="service-name">OILFLOW'S (0)</div>
  </div>
  <div class="service" style="left:593px">
    <div class="service-tile"><svg width="46" height="40" viewBox="0 0 46 40"><path d="M23 4c4 6 6 9 6 12a6 6 0 0 1-12 0c0-3 2-6 6-12z" fill="var(--navy)"/><path d="M3 26h40l-4 8H7z" fill="var(--navy)"/><path d="M3 24h40" stroke="var(--navy)" stroke-width="2"/></svg></div>
    <div class="service-name">DRAINFLOW'S (0)</div>
  </div>
  <div class="service" style="left:779px">
    <div class="service-tile"><svg width="30" height="40" viewBox="0 0 30 40"><path d="M18 2L5 23h9l-4 15 15-22h-9z" fill="var(--navy)"/></svg></div>
    <div class="service-name">POWERFLOW'S (0)</div>
  </div>
  <div class="service" style="left:966px">
    <div class="service-tile"><svg width="34" height="38" viewBox="0 0 34 38"><path d="M17 2l14 5v10c0 10-6 16-14 19C9 33 3 27 3 17V7z" fill="var(--navy)"/><path d="M17 8l9 3v6c0 6-4 10-9 12-5-2-9-6-9-12v-6z" fill="#fff"/><path d="M12 18l4 4 7-8" fill="none" stroke="var(--navy)" stroke-width="3"/></svg></div>
    <div class="service-name">SECUREFLOW'S (0)</div>
  </div>
</section>

<div class="abs promo promo-boiler" role="img" aria-label="Photo of an engineer adjusting a boiler control panel, fading into a blue overlay">
  <div class="abs promo-boiler-title">Boiler Repairs<br>&amp; MAINTENANCE</div>
</div>
<div class="abs promo promo-move" role="img" aria-label="Photo of a mother and daughter unpacking cardboard boxes in a kitchen">
  <div class="abs promo-move-title">MOVING HOME?</div>
  <div class="abs promo-move-text">We are here to help things go as smoothly possible.</div>
  <svg class="abs btn-arrow" width="160" height="40" viewBox="0 0 160 40"><path d="M0 0h140l20 20-20 20H0z" fill="var(--orange)"/><text x="19" y="25" fill="#fff" font-family="Open Sans, Arial, sans-serif" font-size="14">MOVE HOME</text></svg>
</div>

<section class="abs testimonial" role="img" aria-label="Photo of a smiling plumber in a blue cap working under a kitchen sink"></section>
<div class="abs quote-card">
  <h2 class="quote-title">HAPPY CLIENTS</h2>
  <p class="quote-text">Just to let you know your crew the best company that I've ever had working with! They were extremely professional, very polite, and the exceptional. The manner and speed they did this job was remarkable. family really can't recommend this company highly enough.</p>
</div>
<div class="abs quote-mark">&ldquo;</div>
<svg class="abs quote-pointer" width="30" height="16" viewBox="0 0 30 16"><path d="M0 0h30L15 15z" fill="#fff"/></svg>
<div class="abs avatar" role="img" aria-label="Client portrait"></div>
<div class="abs client-name">Marcus T.</div>
<div class="abs client-place">Elmbrook, NY</div>

<div class="abs footer-bg"></div>
<section class="abs featured"></section>
<h2 class="abs featured-title">OUR FEATURED WORK</h2>
<div class="work" style="left:97px">
  <div class="work-photo" role="img" aria-label="Photo of a plumber fitting pipes under a sink" style="background:linear-gradient(120deg,#cfd3d8,#7a8594 60%,#454c57)"></div>
  <div class="work-title">PLUMBING WORKER</div>
  <p class="work-text">simply dummy text of the printing and typesetting industry. Lorem Ipsum has been the industry's standard dummy text ever since the 1500s</p>
</div>
<div class="work" style="left:354px">
  <div class="work-photo" role="img" aria-label="Photo of hands tightening a radiator valve" style="background:linear-gradient(120deg,#ece9e4,#b9a690 55%,#8a7560)"></div>
  <div class="work-title">HEATING COMPANY</div>
  <p class="work-text">simply dummy text of the printing and typesetting industry. Lorem Ipsum has been the industry's.</p>
</div>
<div class="work" style="left:613px">
  <div class="work-photo" role="img" aria-label="Photo of a red wrench on a chrome pipe" style="background:linear-gradient(120deg,#4f6f9a,#c8ced6 50%,#b44a3e)"></div>
  <div class="work-title">PLUMBING SERVICES</div>
  <p class="work-text">simply dummy text of the printing and typesetting industry. Lorem Ipsum has been the industry's standard dummy text ever since the 1500s</p>
</div>
<div class="work" style="left:872px">
  <div class="work-photo" role="img" aria-label="Photo of a family unpacking boxes in a new home" style="background:linear-gradient(120deg,#d8d3c8,#b89d7a 55%,#8c7760)"></div>
  <div class="work-title">HOUSE MOVE</div>
  <p class="work-text">simply dummy text of the printing and typesetting industry. Lorem Ipsum has been the industry's.</p>
</div>

<footer>
  <div class="footer-col" style="left:97px">
    <h3 class="footer-heading">AT HOME</h3>
    <ul class="footer-links"><li>Moving Home</li><li>Our Guarantee</li><li>Charges</li><li>My Bill</li><li>Emergencies</li><li>Got a problem?</li></ul>
  </div>
  <div class="footer-col" style="left:330px">
    <h3 class="footer-heading">BUSINESS CUSTOMERS</h3>
    <ul class="footer-links"><li>Business services</li><li>Landlord services</li><li>Estate Agents</li><li>Property Contracts</li><li>Commercial Installations</li><li>Commercial Gas</li></ul>
  </div>
  <div class="footer-col" style="left:599px">
    <h3 class="footer-heading">NEW BUILDS &amp; CONSTRUCTION</h3>
    <ul class="footer-links"><li>Heating and Water Design</li><li>Heating Technology</li><li>Housing Estates</li><li>Single Dwelling Install</li><li>Multi Dwelling Installs</li><li>Aftercare Guarantee</li></ul>
  </div>
  <div class="footer-col" style="left:926px">
    <h3 class="footer-heading">AT HOME</h3>
    <ul class="footer-links"><li>About us</li><li>Legal</li><li>Cookie policy</li><li>Access for everyone</li><li>Complaints procedure</li><li>Codes of practice</li></ul>
  </div>
  <div class="abs legal"></div>
  <div class="abs legal-left"><span>Terms &amp; conditions</span><span>|</span><span>Privacy policy</span></div>
  <div class="abs legal-right">© 2016 Brackwell Flow's UK Limited, All rights reserved. Registered in England and Wales</div>
</footer>

</body>
</html>
```